Business Card Design Project

Business Card
We are rebranding with a new logo
Industry/Entity Type
Business
Contact Information for Business Card
Dennis Marlow +61 427581962 dennis@qovo.com.au P.O. Box 872 Kelvindale QLD 4309
Requirements
Must have
- Logo

```html
<!DOCTYPE html>
<html lang="en">
<head>
<meta charset="utf-8">
<title>Qovo International – Dennis Marlow</title>
<link rel="stylesheet" href="https://fonts.googleapis.com/css2?family=Merriweather+Sans:wght@800&family=Fira+Sans:wght@500;600&family=Libre+Franklin:wght@400&display=swap">
<style>
  :root {
    --paper: #f4f4f4;
    --paper-edge: #e2e2e2;
    --ink: #1c1c1c;
    --ink-soft: #7a7a7a;
    --brand-blue: #1a8ad4;
    --brand-orange: #ff6a0d;
    --band-light: #8fdce6;
    --band-dark: #4a5584;
  }
  html, body { margin: 0; padding: 0; overflow: hidden; background: #ffffff; }
  .card {
    position: relative;
    width: 717px;
    height: 1200px;
    overflow: hidden;
    background: radial-gradient(ellipse at 50% 45%, #fbfbfb 0%, var(--paper) 55%, var(--paper-edge) 100%);
  }
  .card__band { position: absolute; left: 0; bottom: 0; width: 717px; height: 310px; }
  .brand {
    position: absolute;
    top: 262px; left: 0; width: 717px;
    text-align: center;
    font-family: "Fira Sans", sans-serif;
    font-weight: 600;
    font-size: 50px;
    letter-spacing: 2px;
    color: var(--brand-blue);
    margin: 0;
  }
  .person { position: absolute; top: 524px; left: 164px; width: 380px; }
  .person__name {
    margin: 0;
    font-family: "Merriweather Sans", sans-serif;
    font-weight: 800;
    font-size: 41px;
    letter-spacing: 1px;
    text-transform: uppercase;
    color: var(--ink);
    line-height: 1.1;
    white-space: nowrap;
  }
  .person__surname { color: var(--ink-soft); }
  .person__role {
    margin: 4px 0 0 98px;
    font-family: "Fira Sans", sans-serif;
    font-weight: 500;
    font-size: 31px;
    color: var(--brand-blue);
    text-transform: uppercase;
  }
  .contacts {
    position: absolute;
    top: 670px; left: 169px;
    margin: 0; padding: 0; list-style: none;
    font-family: "Libre Franklin", sans-serif;
    font-size: 29px;
    color: var(--ink);
  }
  .contacts__item { display: flex; align-items: flex-start; margin-bottom: 14px; }
  .contacts__icon { width: 41px; height: 42px; flex: none; margin-right: 39px; }
  .contacts__text { line-height: 36px; padding-top: 3px; white-space: nowrap; }
</style>
</head>
<body>
<div class="card">
  <svg class="card__band" viewBox="0 0 717 310" role="img" aria-label="Decorative curved colour band along the bottom edge">
    <defs>
      <linearGradient id="bandFill" x1="0" y1="0" x2="1" y2="1">
        <stop offset="0" stop-color="var(--band-light)"/>
        <stop offset="1" stop-color="var(--band-dark)"/>
      </linearGradient>
    </defs>
    <path d="M0,60 C200,120 450,20 717,50 L717,310 L0,310 Z" fill="url(#bandFill)"/>
  </svg>

  <p class="brand">Qovo International</p>

  <div class="person">
    <h1 class="person__name">Dennis <span class="person__surname">Marlow</span></h1>
    <p class="person__role">Job Title</p>
  </div>

  <ul class="contacts">
    <li class="contacts__item">
      <svg class="contacts__icon" viewBox="0 0 41 42" aria-hidden="true">
        <rect width="41" height="42" rx="4" fill="var(--brand-orange)"/>
        <path d="M12,9 L17,9 L19,15 L16,17 C17.5,21 20,24 24,26 L26,23 L32,25 L32,30 C32,32 30,33 28,33 C18,32 10,24 9,13 C9,11 10,9 12,9 Z" fill="#fff"/>
      </svg>
      <span class="contacts__text">+61 427581962</span>
    </li>
    <li class="contacts__item">
      <svg class="contacts__icon" viewBox="0 0 41 42" aria-hidden="true">
        <rect width="41" height="42" rx="4" fill="var(--brand-orange)"/>
        <rect x="6" y="12" width="25" height="18" fill="none" stroke="#fff" stroke-width="2"/>
        <path d="M6,12 L18.5,22 L31,12" fill="none" stroke="#fff" stroke-width="2"/>
      </svg>
      <span class="contacts__text">dennis@qovo.com.au</span>
    </li>
    <li class="contacts__item">
      <svg class="contacts__icon" viewBox="0 0 41 42" aria-hidden="true">
        <rect width="41" height="42" rx="4" fill="var(--brand-orange)"/>
        <path d="M11,34 L11,15 C11,10 15,7 20.5,7 C26,7 30,10 30,15 L30,34 Z" fill="#fff"/>
        <rect x="14" y="16" width="13" height="8" fill="var(--brand-orange)"/>
        <rect x="16" y="18" width="9" height="4" fill="#fff"/>
        <rect x="19" y="27" width="3" height="7" fill="var(--brand-orange)"/>
      </svg>
      <span class="contacts__text">P.O. Box 872 Kelvindale<br>QLD 4309</span>
    </li>
  </ul>
</div>
</body>
</html>
```